Master slides for standard ppt presentation

I just my company, went through Emblemyard for the log design and already have an identity that I like.
I need to transpose this identity into some nice Master slides for Powerpoint presentation. I want it clean, with fresh color connection to my logo, not over crowded and obviously different vs what powerpoint proposes as standard design ideas. I will attach a few materials that I already use, branded with the company logo so that you can take inspiration.

```html
<!DOCTYPE html>
<html lang="en">
<head>
<meta charset="utf-8">
<title>Verdantia Master Slides</title>
<link href="https://fonts.googleapis.com/css2?family=Poppins:ital,wght@0,400;0,500;0,600;0,700;1,600;1,800&family=Roboto:wght@400;500&display=swap" rel="stylesheet">
<style>
:root{
  --canvas:#dfe0e2;
  --forest:#17463f;
  --forest-deep:#123a34;
  --leaf:#4dbb7b;
  --mint:#8fd3a8;
  --grey:#b9bcbc;
  --ink:#3a3a3a;
  --body:#8a8d8c;
  --white:#ffffff;
}
*{margin:0;padding:0;box-sizing:border-box}
html,body{width:1200px;height:1112px;overflow:hidden;background:var(--canvas)}
body{position:relative;font-family:"Poppins",sans-serif}
.slide{position:absolute;width:256px;height:144px;background:var(--white);overflow:hidden;box-shadow:0 2px 4px rgba(0,0,0,.12)}
.slide .footer{position:absolute;left:0;right:0;bottom:0;height:5px;background:var(--forest);color:#cfe3dc;font-size:2.4px;text-align:center;line-height:5px;font-family:"Roboto",sans-serif}
.brand{font-family:"Poppins",sans-serif;font-weight:700;color:var(--forest);letter-spacing:.02em;white-space:nowrap}
.brand-mark{display:inline-block;width:5px;height:5px;background:var(--leaf);margin-right:2px;vertical-align:middle}
.brand.small{position:absolute;font-size:4.6px}
.brand.on-dark{color:var(--white)}
.heading{position:absolute;font-weight:600;font-size:9.5px;color:var(--forest);line-height:1.05}
.heading .sub{display:block;font-weight:400;font-size:5px;color:var(--leaf);margin-top:1px}
.heading.light{color:var(--white)}
.heading.light .sub{color:#cfe3dc}
.para{position:absolute;font-family:"Roboto",sans-serif;font-size:3.1px;line-height:4.4px;color:var(--body);text-align:justify}
.para.light{color:#d6e6e1}
.para + .para{}
.photo{position:absolute}
.col-title{font-family:"Poppins",sans-serif;font-size:3.6px;font-weight:600;color:var(--ink);margin-bottom:1px}
.group{margin-bottom:4px}
svg{display:block}
</style>
</head>
<body>

<!-- Row 1 -->
<section class="slide cover-photo" style="left:180px;top:70px">
  <div class="photo" role="img" aria-label="City skyline photo with green tint" style="inset:0;background:linear-gradient(180deg,#5fb89a 0%,#3f9887 45%,#2e7d73 75%,#3b8d80 100%)"></div>
  <div class="brand small on-dark" style="left:22px;top:22px;font-size:6px">VERDANTIA</div>
  <div style="position:absolute;left:22px;top:90px;color:#fff">
    <div style="font-weight:800;font-style:italic;font-size:17px;line-height:1">About</div>
    <div style="font-weight:600;font-style:italic;font-size:9px;line-height:1.2">Title Presentation</div>
    <div style="width:12px;height:1px;background:#fff;margin:2px 0"></div>
    <div style="font-style:italic;font-size:5px">Sub Title Presentation Goes Here</div>
  </div>
</section>

<section class="slide cover-light" style="left:472px;top:70px">
  <div class="brand small" style="left:16px;top:48px;font-size:6px">VERDANTIA</div>
  <div style="position:absolute;left:16px;top:80px">
    <div style="font-weight:800;font-style:italic;font-size:17px;line-height:1;color:var(--forest)">About</div>
    <div style="font-weight:600;font-style:italic;font-size:9px;line-height:1.2;color:var(--forest)">Title Presentation</div>
    <div style="width:14px;height:1.5px;background:var(--leaf);margin:3px 0"></div>
    <div style="font-style:italic;font-size:5px;color:var(--body)">Sub Title Presentation Goes Here</div>
  </div>
  <div class="footer">Copyright © 2023 Verdantia</div>
</section>

<section class="slide company" style="left:763px;top:70px">
  <div class="brand small" style="right:8px;top:14px">VERDANTIA</div>
  <div style="position:absolute;left:0;right:0;top:30px;text-align:center;font-size:3px;color:var(--body)">YOUR BUSINESS SOLUTIONS</div>
  <div style="position:absolute;left:0;right:0;top:34px;text-align:center;font-size:7.5px;font-weight:500;color:var(--ink)">COMPANY NAME</div>
  <div class="para" style="left:48px;width:160px;top:50px;text-align:center">Our team builds clear plans that help each client grow with steady simple steps and honest advice every single year.</div>
  <div style="position:absolute;left:114px;top:81px;width:30px;height:7px;border-radius:4px;background:var(--leaf);color:#fff;font-size:3.5px;text-align:center;line-height:7px">Learn More</div>
  <div style="position:absolute;left:0;right:0;top:104px;text-align:center;font-size:3.5px;letter-spacing:.15em;color:var(--body)">www.northlinestudio.example</div>
  <div class="photo" role="img" aria-label="Line drawing of a city skyline" style="left:0;right:0;top:100px;height:39px;background:linear-gradient(180deg,rgba(23,70,63,0) 0%,rgba(23,70,63,.12) 100%)"></div>
  <div class="footer">Copyright © 2023 Verdantia</div>
</section>

<!-- Row 2 -->
<section class="slide split-intro" style="left:180px;top:235px">
  <svg width="256" height="144" style="position:absolute;inset:0"><path d="M150 0 Q118 72 150 144 H256 V0 Z" fill="var(--forest)"/></svg>
  <div class="brand" style="position:absolute;left:17px;top:98px;font-size:15px">VERDANTIA</div>
  <div class="heading light" style="left:144px;top:15px">Heading Here<span class="sub" style="font-size:4px">Sub Heading</span></div>
  <div class="para light" style="left:144px;top:38px;width:98px">Our team builds clear plans that help each client grow with steady simple steps and honest advice every single year. We listen first, shape ideas together, and deliver work that stays useful long after launch, keeping every detail calm, fresh and easy to share.</div>
  <div class="para light" style="left:144px;top:105px;width:98px">Our team builds clear plans that help each client grow with steady simple steps and honest advice every single year.</div>
</section>

<section class="slide dark-text" style="left:472px;top:235px;background:var(--forest)">
  <div class="brand small on-dark" style="right:12px;top:16px">VERDANTIA</div>
  <div class="heading light" style="left:24px;top:22px">Heading Here<span class="sub" style="font-size:4px">Sub Heading</span></div>
  <div class="para light" style="left:24px;top:45px;width:84px">Our team builds clear plans that help each client grow with steady simple steps and honest advice every single year. We listen first, shape ideas together, and deliver work that stays useful long after launch, keeping every detail calm, fresh and easy to share.</div>
  <div class="para light" style="left:24px;top:100px;width:84px">Our team builds clear plans that help each client grow with steady simple steps and honest advice every single year.</div>
</section>

<section class="slide groups" style="left:763px;top:235px">
  <div class="brand small" style="right:8px;top:14px">VERDANTIA</div>
  <div class="heading" style="left:18px;top:12px">Heading Here<span class="sub">Sub Heading</span></div>
  <div style="position:absolute;left:18px;top:38px;width:102px">
    <div class="group"><div class="col-title">Group 1</div><div class="para" style="position:static">Our team builds clear plans that help each client grow with steady simple steps and honest advice every single year.</div></div>
    <div class="group"><div class="col-title">Group 1</div><div class="para" style="position:static">Our team builds clear plans that help each client grow with steady simple steps and honest advice every single year.</div></div>
    <div class="group"><div class="col-title">Group 1</div><div class="para" style="position:static">Our team builds clear plans that help each client grow with steady simple steps and honest advice every single year.</div></div>
  </div>
  <div style="position:absolute;left:136px;top:38px;width:102px">
    <div class="group"><div class="col-title">Group 1</div><div class="para" style="position:static">Our team builds clear plans that help each client grow with steady simple steps and honest advice every single year.</div></div>
    <div class="group"><div class="col-title">Group 1</div><div class="para" style="position:static">Our team builds clear plans that help each client grow with steady simple steps and honest advice every single year.</div></div>
    <div class="group"><div class="col-title">Group 1</div><div class="para" style="position:static">Our team builds clear plans that help each client grow with steady simple steps and honest advice every single year.</div></div>
  </div>
  <div class="footer">Copyright © 2023 Verdantia</div>
</section>

<!-- Row 3 -->
<section class="slide bar-chart" style="left:180px;top:401px">
  <div class="brand small" style="right:8px;top:14px">VERDANTIA</div>
  <div class="heading" style="left:16px;top:13px">Heading Here<span class="sub" style="color:var(--ink);font-size:4.5px">Sub Heading</span></div>
  <svg width="256" height="144" style="position:absolute;inset:0" font-family="Roboto,sans-serif" font-size="3" fill="#999">
    <g stroke="#eee" stroke-width=".4"><line x1="36" y1="55" x2="245" y2="55"/><line x1="36" y1="68" x2="245" y2="68"/><line x1="36" y1="81" x2="245" y2="81"/><line x1="36" y1="94" x2="245" y2="94"/><line x1="36" y1="107" x2="245" y2="107"/></g>
    <text x="30" y="56">125</text><text x="30" y="69">100</text><text x="32" y="82">75</text><text x="32" y="95">50</text><text x="32" y="108">25</text><text x="34" y="121">0</text>
    <rect x="40" y="112" width="9" height="8" fill="var(--grey)"/><rect x="50" y="95" width="9" height="25" fill="var(--forest)"/><rect x="60" y="103" width="9" height="17" fill="var(--leaf)"/>
    <rect x="90" y="108" width="9" height="12" fill="var(--grey)"/><rect x="100" y="102" width="9" height="18" fill="var(--leaf)"/><rect x="110" y="80" width="9" height="40" fill="var(--forest)"/>
    <rect x="140" y="95" width="9" height="25" fill="var(--leaf)"/><rect x="150" y="84" width="9" height="36" fill="var(--forest)"/><rect x="160" y="104" width="9" height="16" fill="var(--grey)"/>
    <rect x="190" y="70" width="9" height="50" fill="var(--forest)"/><rect x="200" y="90" width="9" height="30" fill="var(--leaf)"/><rect x="210" y="106" width="9" height="14" fill="var(--grey)"/>
    <line x1="36" y1="120" x2="245" y2="120" stroke="#ccc" stroke-width=".4"/>
    <text x="55" y="124">April</text><text x="105" y="124">May</text>
    <rect x="44" y="132" width="3" height="3" fill="var(--forest)"/><text x="49" y="134.5">Sample Series</text>
    <rect x="97" y="132" width="3" height="3" fill="var(--grey)"/><text x="102" y="134.5">Sample Series</text>
    <rect x="150" y="132" width="3" height="3" fill="var(--forest)"/><text x="155" y="134.5">Sample Series</text>
    <rect x="203" y="132" width="3" height="3" fill="#ddd"/><text x="208" y="134.5">Sample Series</text>
  </svg>
</section>

<section class="slide contents" style="left:472px;top:401px">
  <div class="photo" role="img" aria-label="Photo of a team working together at a laptop" style="left:0;top:0;width:112px;height:139px;background:linear-gradient(135deg,#5e5a55 0%,#8d8a84 45%,#c9c5be 100%)"></div>
  <div style="position:absolute;left:136px;top:12px;font-size:6px;font-weight:600;color:var(--forest)">TABLE OF CONTENT</div>
  <div class="brand small" style="right:8px;top:12px">VERDANTIA</div>
  <svg width="256" height="144" style="position:absolute;inset:0" font-family="Poppins,sans-serif">
    <g fill="var(--forest)"><circle cx="122" cy="40" r="7"/><circle cx="122" cy="65" r="7"/><circle cx="122" cy="89" r="7"/><circle cx="122" cy="114" r="7"/></g>
    <g fill="none" stroke="#cfd8d5" stroke-width=".6"><circle cx="122" cy="40" r="9"/><circle cx="122" cy="65" r="9"/><circle cx="122" cy="89" r="9"/><circle cx="122" cy="114" r="9"/></g>
    <g fill="#fff" font-size="5" font-weight="600" text-anchor="middle"><text x="122" y="42">01</text><text x="122" y="67">02</text><text x="122" y="91">03</text><text x="122" y="116">04</text></g>
  </svg>
  <div style="position:absolute;left:136px;top:34px;width:110px">
    <div class="col-title" style="font-size:3.4px;color:var(--forest)">LOREM IPSUM</div>
    <div class="para" style="position:static">Our team builds clear plans that help each client grow with steady simple steps and honest advice every single year.</div>
  </div>
  <div style="position:absolute;left:136px;top:59px;width:110px">
    <div class="col-title" style="font-size:3.4px;color:var(--forest)">LOREM IPSUM</div>
    <div class="para" style="position:static">Our team builds clear plans that help each client grow with steady simple steps and honest advice every single year.</div>
  </div>
  <div style="position:absolute;left:136px;top:83px;width:110px">
    <div class="col-title" style="font-size:3.4px;color:var(--forest)">LOREM IPSUM</div>
    <div class="para" style="position:static">Our team builds clear plans that help each client grow with steady simple steps and honest advice every single year.</div>
  </div>
  <div style="position:absolute;left:136px;top:108px;width:110px">
    <div class="col-title" style="font-size:3.4px;color:var(--forest)">LOREM IPSUM</div>
    <div class="para" style="position:static">Our team builds clear plans that help each client grow with steady simple steps and honest advice every single year.</div>
  </div>
  <div class="footer">Copyright © 2023 Verdantia</div>
</section>

<section class="slide text-page" style="left:763px;top:401px">
  <div class="brand small" style="right:8px;top:14px">VERDANTIA</div>
  <div class="heading" style="left:18px;top:13px">Heading Here<span class="sub">Sub Heading</span></div>
  <div class="para" style="left:18px;top:40px;width:220px">Our team builds clear plans that help each client grow with steady simple steps and honest advice every single year. We listen first, shape ideas together, and deliver work that stays useful long after launch, keeping every detail calm, fresh and easy to share.</div>
  <div class="para" style="left:18px;top:62px;width:220px">Our team builds clear plans that help each client grow with steady simple steps and honest advice every single year. We listen first, shape ideas together, and deliver work that stays useful long after launch, keeping every detail calm, fresh and easy to share.</div>
  <div class="para" style="left:18px;top:84px;width:220px">Our team builds clear plans that help each client grow with steady simple steps and honest advice every single year. We listen first, shape ideas together, and deliver work that stays useful long after launch, keeping every detail calm, fresh and easy to share.</div>
  <div class="para" style="left:18px;top:106px;width:220px">Our team builds clear plans that help each client grow with steady simple steps and honest advice every single year. We listen first, shape ideas together, and deliver work that stays useful long after launch, keeping every detail calm, fresh and easy to share.</div>
  <div class="footer">Copyright © 2023 Verdantia</div>
</section>

<!-- Row 4 -->
<section class="slide heading-left" style="left:180px;top:566px">
  <div class="brand small" style="left:12px;top:14px">VERDANTIA</div>
  <div class="heading" style="left:22px;top:65px;font-size:11px">Heading Here<span class="sub" style="color:var(--ink);font-size:6px">Sub Heading</span></div>
  <div class="para" style="left:127px;top:35px;width:111px">Our team builds clear plans that help each client grow with steady simple steps and honest advice every single year. We listen first, shape ideas together, and deliver work that stays useful long after launch, keeping every detail calm, fresh and easy to share.</div>
  <div class="para" style="left:127px;top:93px;width:111px">Our team builds clear plans that help each client grow with steady simple steps and honest advice every single year.</div>
  <div class="footer">Copyright © 2023 Verdantia</div>
</section>

<section class="slide photo-right" style="left:472px;top:566px">
  <div class="heading" style="left:16px;top:21px">Heading Here<span class="sub" style="color:var(--ink)">Sub Heading</span></div>
  <div class="para" style="left:16px;top:55px;width:102px">Our team builds clear plans that help each client grow with steady simple steps and honest advice every single year. We listen first, shape ideas together, and deliver work that stays useful long after launch, keeping every detail calm, fresh and easy to share.</div>
  <div class="photo" role="img" aria-label="Photo of a group of colleagues gathered around a laptop" style="left:135px;top:0;width:121px;height:139px;background:linear-gradient(160deg,#d9d6cf 0%,#8a7a6c 45%,#3b3431 100%)"></div>
  <div class="footer">Copyright © 2023 Verdantia</div>
</section>

<section class="slide pie" style="left:763px;top:566px">
  <div class="brand small" style="right:8px;top:14px">VERDANTIA</div>
  <div class="heading" style="left:18px;top:13px">Heading Here<span class="sub">Sub Heading</span></div>
  <div class="para" style="left:18px;top:38px;width:96px">Our team builds clear plans that help each client grow with steady simple steps and honest advice every single year.</div>
  <div class="para" style="left:18px;top:100px;width:96px">Our team builds clear plans that help each client grow with steady simple steps and honest advice every single year.</div>
  <svg width="256" height="144" style="position:absolute;inset:0" font-family="Roboto,sans-serif">
    <path d="M205 75 L205 47 A28 28 0 0 1 232.5 69.8 Z" fill="var(--leaf)"/>
    <path d="M205 75 L232.5 69.8 A28 28 0 0 1 220 98.6 Z" fill="var(--grey)"/>
    <path d="M205 75 L220 98.6 A28 28 0 1 1 205 47 Z" fill="var(--forest)"/>
    <g fill="#fff" font-size="3.2"><text x="216" y="56">22%</text><text x="224" y="80">19%</text><text x="186" y="94">58%</text></g>
    <g font-size="3.2" fill="#333">
      <rect x="173" y="122" width="2.5" height="2.5" fill="var(--forest)"/><text x="177" y="124.5">Sale</text>
      <rect x="187" y="122" width="2.5" height="2.5" fill="var(--leaf)"/><text x="191" y="124.5">Revenue</text>
      <rect x="207" y="122" width="2.5" height="2.5" fill="var(--forest)"/><text x="211" y="124.5">Profit</text>
      <rect x="222" y="122" width="2.5" height="2.5" fill="var(--grey)"/><text x="226" y="124.5">Expenditure</text>
    </g>
  </svg>
  <div class="footer">Copyright © 2023 Verdantia</div>
</section>

<!-- Row 5 -->
<section class="slide thanks" style="left:180px;top:731px;background:var(--forest);color:#fff;text-align:center;font-family:'Roboto',sans-serif">
  <div style="position:absolute;left:0;right:0;top:27px;font-size:23px;line-height:1.2">Thanks<br>&nbsp;&nbsp;&nbsp;For Wathing</div>
  <div style="position:absolute;left:0;right:0;top:92px;font-size:6.3px;line-height:1.45">Lakeside, Western Region<br>P : 0040 700 000 111&nbsp; E : lucas.morel@verdantia.example<br>www.verdantia.example</div>
</section>

<section class="slide photo-left" style="left:472px;top:731px">
  <div class="photo" role="img" aria-label="Photo of a person working on a laptop at a desk" style="left:0;top:0;width:122px;height:139px;background:linear-gradient(135deg,#6a5f52 0%,#a9a195 50%,#dcd8cf 100%)"></div>
  <div class="brand small" style="right:8px;top:13px">VERDANTIA</div>
  <div class="heading" style="left:137px;top:10px">Heading Here<span class="sub" style="color:var(--ink);font-size:4.5px">Sub Heading</span></div>
  <div class="para" style="left:137px;top:38px;width:108px">Our team builds clear plans that help each client grow with steady simple steps and honest advice every single year. We listen first, shape ideas together, and deliver work that stays useful long after launch, keeping every detail calm, fresh and easy to share.</div>
  <div class="para" style="left:137px;top:99px;width:108px">Our team builds clear plans that help each client grow with steady simple steps and honest advice every single year.</div>
  <div class="footer">Copyright © 2023 Verdantia</div>
</section>

<section class="slide grouped-bars" style="left:763px;top:731px">
  <svg width="256" height="144" style="position:absolute;inset:0" font-family="Roboto,sans-serif" font-size="2.6" fill="#999">
    <g stroke="#eee" stroke-width=".4"><line x1="24" y1="22" x2="240" y2="22"/><line x1="24" y1="30" x2="240" y2="30"/><line x1="24" y1="38" x2="240" y2="38"/><line x1="24" y1="46" x2="240" y2="46"/><line x1="24" y1="54" x2="240" y2="54"/><line x1="24" y1="62" x2="240" y2="62"/></g>
    <g fill="#aaa"><text x="19" y="23">6</text><text x="19" y="31">5</text><text x="19" y="39">4</text><text x="19" y="47">3</text><text x="19" y="55">2</text><text x="19" y="63">1</text></g>
    <rect x="32" y="34" width="7" height="36" fill="var(--forest)"/><rect x="40" y="52" width="7" height="18" fill="#5a5a5a"/><rect x="48" y="50" width="7" height="20" fill="var(--leaf)"/><rect x="56" y="54" width="7" height="16" fill="#ccc"/>
    <rect x="84" y="52" width="7" height="18" fill="var(--forest)"/><rect x="92" y="33" width="7" height="37" fill="var(--leaf)"/><rect x="100" y="55" width="7" height="15" fill="#5a5a5a"/><rect x="108" y="50" width="7" height="20" fill="#ccc"/>
    <rect x="136" y="40" width="7" height="30" fill="var(--forest)"/><rect x="144" y="50" width="7" height="20" fill="var(--leaf)"/><rect x="152" y="53" width="7" height="17" fill="#ccc"/><rect x="160" y="35" width="7" height="35" fill="#5a5a5a"/>
    <rect x="188" y="36" width="7" height="34" fill="var(--leaf)"/><rect x="196" y="44" width="7" height="26" fill="var(--forest)"/><rect x="204" y="28" width="7" height="42" fill="var(--forest)"/><rect x="212" y="34" width="7" height="36" fill="#ccc"/>
    <line x1="24" y1="70" x2="240" y2="70" stroke="#ccc" stroke-width=".4"/>
    <text x="42" y="74">2014</text><text x="94" y="74">2015</text><text x="146" y="74">2016</text><text x="198" y="74">2017</text>
    <rect x="38" y="78" width="2" height="2" fill="var(--leaf)"/><text x="41" y="80">Series One</text>
    <rect x="68" y="78" width="2" height="2" fill="var(--forest)"/><text x="71" y="80">Series Two</text>
    <rect x="98" y="78" width="2" height="2" fill="var(--forest)"/><text x="101" y="80">Series Three</text>
    <rect x="130" y="78" width="2" height="2" fill="#ccc"/><text x="133" y="80">Series Four</text>
  </svg>
  <div class="para" style="left:18px;top:91px;width:222px">Our team builds clear plans that help each client grow with steady simple steps and honest advice every single year. We listen first, shape ideas together, and deliver work that stays useful long after launch, keeping every detail calm, fresh and easy to share.</div>
  <div class="footer">Copyright © 2023 Verdantia</div>
</section>

<!-- Row 6 -->
<section class="slide icon-set" style="left:180px;top:895px">
  <div class="photo" role="img" aria-label="Grid of small black interface and business icons" style="left:22px;top:14px;width:212px;height:120px;background:linear-gradient(180deg,#e9eaea 0%,#dcdede 100%);border-radius:2px"></div>
</section>

<section class="slide contact-card" style="left:472px;top:895px">
  <svg width="256" height="144" style="position:absolute;inset:0"><path d="M150 0 Q120 20 123 60 Q126 110 115 144 H256 V0 Z" fill="var(--forest)"/></svg>
  <div class="brand" style="position:absolute;left:17px;top:95px;font-size:15px">VERDANTIA</div>
  <div style="position:absolute;left:138px;top:15px;color:#fff">
    <div style="font-weight:700;font-size:12.5px;line-height:1.1">Lucas Morel</div>
    <div style="font-size:7.5px;line-height:1.2">Managing Partner</div>
  </div>
  <div style="position:absolute;left:138px;top:75px;color:#fff;font-family:'Roboto',sans-serif;font-size:6.4px;line-height:1.15">14 Harbour Lane,<br>Eastfield, ON L0A 1B2</div>
  <svg width="256" height="144" style="position:absolute;inset:0" fill="#fff">
    <circle cx="141" cy="105" r="2.8"/><circle cx="141" cy="116" r="2.8"/><circle cx="141" cy="126" r="2.8"/>
    <path d="M140 104 l1 0 .6 1.2 -.5 .5 a3 3 0 0 0 1.2 1.2 l.5-.5 1.2.6 0 1" fill="var(--forest)"/>
    <circle cx="141" cy="116" r="1.3" fill="none" stroke="var(--forest)" stroke-width=".5"/>
    <circle cx="141" cy="126" r="1.6" fill="none" stroke="var(--forest)" stroke-width=".5"/><line x1="139.4" y1="126" x2="142.6" y2="126" stroke="var(--forest)" stroke-width=".4"/>
  </svg>
  <div style="position:absolute;left:146px;top:101.5px;color:#fff;font-family:'Roboto',sans-serif;font-size:6.4px;line-height:10.5px">0040 700 000 111<br>lucas.morel@verdantia.example<br>www.verdantia.example</div>
</section>

<section class="slide bridge" style="left:763px;top:895px">
  <div class="brand small" style="right:8px;top:17px">VERDANTIA</div>
  <div class="heading" style="left:18px;top:17px">Heading Here<span class="sub">Sub Heading</span></div>
  <div class="para" style="left:18px;top:38px;width:222px">Our team builds clear plans that help each client grow with steady simple steps and honest advice every single year. We listen first, shape ideas together, and deliver work that stays useful long after launch, keeping every detail calm, fresh and easy to share.</div>
  <div class="para" style="left:18px;top:61px;width:222px">Our team builds clear plans that help each client grow with steady simple steps and honest advice every single year. We listen first, shape ideas together, and deliver work that stays useful long after launch, keeping every detail calm, fresh and easy to share.</div>
  <div class="photo" role="img" aria-label="Illustration of a suspension bridge with the sun" style="left:0;right:0;top:92px;height:47px;background:linear-gradient(180deg,rgba(23,70,63,0) 0%,rgba(23,70,63,.35) 100%)"></div>
  <div class="footer">Copyright © 2023 Verdantia</div>
</section>

</body>
</html>
```